New business card layout design

We need to revamp our business card layout to be more dynamic and professional. Interested in different card materials. Have a logo and color scheme. Possible something dark background light text, see what works. Will attach current card below, along with our favorite card from your website. Please test interesting ideas out with curves vs straight lines, dark background, dark/light sides, inlaid text, etc.

https://www.brivoltholdings.example/
Here is our website for theme. Let us know if you have ANY questions :)

Target Market(s)

high-net worth accredited investors and fund managers

Industry/Entity Type

Oil and Gas investment fund

Contact Information for Business Card

Name, title, number, email, website, possibly barcode to contact page on website, business name and logo

Colors
0054AA
0677BA
7BADD7
CADEEF
E8F1F8

Requirements
Must have
• Name, title, number, email, website
Nice to have
• barcode to contact page, other ideas?
Should not have
• a pink unicorn

```html
<!DOCTYPE html>
<html lang="en">
<head>
<meta charset="utf-8">
<title>Brivolt Holdings – Business Card</title>
<link href="https://fonts.googleapis.com/css2?family=Montserrat:wght@400;500;600;700&display=swap" rel="stylesheet">
<style>
  :root {
    --backdrop: #e9e9ec;
    --navy: #1e1e45;
    --navy-deep: #17173d;
    --steel: #a3a3b5;
    --muted: #9b9cae;
    --paper: #ffffff;
    --ink: #1e1e45;
  }
  * { margin: 0; padding: 0; box-sizing: border-box; }
  html, body {
    width: 1200px; height: 1200px; overflow: hidden;
    background: var(--backdrop);
    font-family: "Montserrat", Arial, sans-serif;
  }
  .canvas { position: relative; width: 1200px; height: 1200px; }

  .card {
    position: absolute; left: 226px; width: 746px; height: 436px;
    border-radius: 25px; overflow: hidden;
  }

  /* Front */
  .card-front { top: 94px; background: var(--navy-deep); }
  .front-brand {
    position: absolute; left: 512px; top: 220px; transform: translateX(-50%);
    text-align: center; color: var(--muted); white-space: nowrap;
  }
  .front-brand .brand-name { font-size: 42px; font-weight: 600; letter-spacing: 1px; line-height: 1; }
  .front-brand .brand-sub { margin-top: 16px; font-size: 13px; font-weight: 600; letter-spacing: 2.5px; }

  /* Back */
  .card-back { top: 618px; background: var(--paper); }
  .back-panel { position: absolute; inset: 0; }
  .back-content {
    position: absolute; left: 536px; top: 0; transform: translateX(-50%);
    text-align: center; color: var(--ink); white-space: nowrap;
  }
  .back-brand-name { position: absolute; left: 50%; transform: translateX(-50%); top: 104px; font-size: 30px; font-weight: 700; letter-spacing: 1px; line-height: 1; }
  .back-brand-sub { position: absolute; left: 50%; transform: translateX(-50%); top: 150px; font-size: 11px; font-weight: 600; letter-spacing: 2px; }
  .person-name { position: absolute; left: 50%; transform: translateX(-50%); top: 188px; font-size: 30px; font-weight: 500; line-height: 1; }
  .person-title { position: absolute; left: 50%; transform: translateX(-50%); top: 222px; font-size: 20px; font-weight: 400; color: var(--muted); }
  .contact-icons { position: absolute; left: 50%; transform: translateX(-50%); top: 265px; display: flex; gap: 6px; }
  .contact-icon { width: 30px; height: 30px; }
  .contact-list { position: absolute; left: 50%; transform: translateX(-50%); top: 309px; list-style: none; font-size: 17px; line-height: 25px; font-weight: 400; }
</style>
</head>
<body>
<main class="canvas">

  <section class="card card-front">
    <div class="front-brand">
      <div class="brand-name">BRIVOLT</div>
      <div class="brand-sub">HOLDINGS</div>
    </div>
  </section>

  <section class="card card-back">
    <svg class="back-panel" width="746" height="436" viewBox="0 0 746 436">
      <polygon points="0,0 354,0 216,236 336,436 0,436" fill="var(--steel)"/>
      <polygon points="0,0 340,0 202,236 322,436 0,436" fill="var(--navy)"/>
    </svg>

    <div class="back-content">
      <div class="back-brand-name">BRIVOLT</div>
      <div class="back-brand-sub">HOLDINGS</div>
      <div class="person-name">Daniel Reyes</div>
      <div class="person-title">CEO</div>

      <div class="contact-icons">
        <svg class="contact-icon" viewBox="0 0 30 30" aria-label="Phone">
          <circle cx="15" cy="15" r="15" fill="var(--navy)"/>
          <rect x="10.5" y="7" width="9" height="16" rx="1.5" fill="none" stroke="#fff" stroke-width="1.6"/>
          <circle cx="15" cy="20.3" r="0.9" fill="#fff"/>
        </svg>
        <svg class="contact-icon" viewBox="0 0 30 30" aria-label="Email">
          <circle cx="15" cy="15" r="15" fill="var(--navy)"/>
          <rect x="7.5" y="10" width="15" height="10.5" rx="1" fill="#fff"/>
          <polyline points="7.8,10.5 15,16 22.2,10.5" fill="none" stroke="var(--navy)" stroke-width="1.3"/>
        </svg>
        <svg class="contact-icon" viewBox="0 0 30 30" aria-label="Website">
          <circle cx="15" cy="15" r="15" fill="var(--navy)"/>
          <g fill="none" stroke="#fff" stroke-width="1.2">
            <circle cx="15" cy="15" r="7"/>
            <ellipse cx="15" cy="15" rx="3" ry="7"/>
            <line x1="8" y1="15" x2="22" y2="15"/>
            <line x1="9" y1="11.5" x2="21" y2="11.5"/>
            <line x1="9" y1="18.5" x2="21" y2="18.5"/>
          </g>
        </svg>
      </div>

      <ul class="contact-list">
        <li>(555) 014 2290</li>
        <li>daniel.reyes@brivoltholdings.example</li>
        <li>brivoltholdings.example</li>
      </ul>
    </div>
  </section>

</main>
</body>
</html>
```